BrambleWorks business card

Looking for business card design that supports our company/software values. We have 2 logo designs at the moment but open to change if you think you can enhance the brand. Check out website www.brambleworks.com.au.

Target Market(s)

Education

Contact Information for Business Card

Name, title, mobile, email and website

Font styles to use
Sans Serif

Colors

Designer to choose colors to be used in the design.

Requirements
Must have
• BrambleWorks logo with tree and tagline on rear side with dark grey background colour

```html
<!DOCTYPE html>
<html lang="en">
<head>
<meta charset="utf-8">
<title>BrambleWorks business card</title>
<link rel="stylesheet" href="https://fonts.googleapis.com/css2?family=Roboto:wght@400&family=Nunito+Sans:wght@400;600&family=Ubuntu:wght@400;500&display=swap">
<style>
  :root {
    --page: #ecebe8;
    --card-grey: #bcbdc0;
    --card-white: #ffffff;
    --leaf-green: #a3b68a;
    --accent-green: #5b8c3a;
    --ink: #1d1d1d;
    --ink-soft: #3a3a3a;
    --mark-grey: #4d4d4f;
    --tagline: #f2f2f2;
  }
  * { box-sizing: border-box; margin: 0; padding: 0; }
  html, body { width: 902px; height: 1200px; overflow: hidden; background: var(--page); }
  .canvas { position: relative; width: 902px; height: 1200px; }
  .card {
    position: absolute; left: 78px; width: 745px; height: 436px;
    border-radius: 18px; overflow: hidden; background: var(--card-grey);
  }
  .card--front { top: 132px; }
  .card--back { top: 636px; }
  .card__shape { position: absolute; inset: 0; }

  .person { position: absolute; left: 40px; top: 64px; }
  .person__name { font-family: "Roboto", sans-serif; font-size: 29px; color: var(--ink); line-height: 1; }
  .person__first { color: var(--accent-green); }
  .person__title {
    font-family: "Nunito Sans", sans-serif; font-size: 17px; color: var(--ink);
    margin-top: 6px; padding: 0 2px 4px 0; display: inline-block;
    border-bottom: 1.5px solid var(--ink-soft); width: 118px;
  }
  .address {
    position: absolute; left: 40px; top: 244px;
    font-family: "Nunito Sans", sans-serif; font-size: 17px; line-height: 22px; color: var(--ink);
  }
  .contacts { position: absolute; left: 40px; top: 313px; list-style: none; }
  .contacts li {
    display: flex; align-items: center; gap: 12px;
    font-family: "Roboto", sans-serif; font-size: 17.5px; line-height: 22px; color: var(--ink-soft);
  }
  .contacts svg { width: 13px; height: 13px; flex: none; }

  .brand-front { position: absolute; left: 420px; top: 110px; width: 300px; text-align: center; }
  .brand-front__dot { width: 70px; height: 70px; border-radius: 50%; background: var(--accent-green); margin: 0 auto 36px; }
  .brand-front__name { font-family: "Ubuntu", sans-serif; font-weight: 400; font-size: 35px; color: var(--ink); }

  .brand-back { position: absolute; left: 118px; top: 140px; display: flex; align-items: center; gap: 40px; }
  .brand-back__dot { width: 150px; height: 150px; border-radius: 50%; background: var(--mark-grey); }
  .brand-back__name { font-family: "Ubuntu", sans-serif; font-weight: 500; font-size: 52px; color: var(--mark-grey); line-height: 1; }
  .brand-back__rule { height: 2px; background: var(--tagline); margin: 12px 0 8px; }
  .brand-back__tagline { font-family: "Ubuntu", sans-serif; font-size: 24px; color: var(--tagline); }
</style>
</head>
<body>
<main class="canvas">
  <section class="card card--front">
    <svg class="card__shape" viewBox="0 0 745 436" aria-hidden="true">
      <path d="M488 0 C395 70 345 190 372 290 C388 350 420 395 462 436 L745 436 L745 0 Z" fill="var(--leaf-green)"/>
      <path d="M522 0 C430 70 380 190 402 290 C416 350 444 398 480 436 L745 436 L745 0 Z" fill="var(--card-white)"/>
    </svg>
    <div class="person">
      <h1 class="person__name"><span class="person__first">Daniel</span> Carter</h1>
      <p class="person__title">CEO/ Founder</p>
    </div>
    <p class="address">12th floor, Orin<br>Tower CDMX</p>
    <ul class="contacts">
      <li><svg viewBox="0 0 16 16"><path d="M3 1l3 3-1.5 2c1 2 2.5 3.5 4.5 4.5L11 9l3 3-2 2C6 13 2 9 1 3z" fill="var(--accent-green)"/></svg>+92 300 4172658</li>
      <li><svg viewBox="0 0 16 16"><path d="M1 5c3-3 11-3 14 0l-2 2-2-1V4H5v2L3 7zM4 9h8l2 5H2z" fill="var(--accent-green)"/></svg>+92 21 35550140-4</li>
      <li><svg viewBox="0 0 16 16"><rect x="1" y="3" width="14" height="10" fill="var(--accent-green)"/><path d="M1 3l7 6 7-6" fill="none" stroke="#fff" stroke-width="1.3"/></svg>dcarter@bramble.com</li>
      <li><svg viewBox="0 0 16 16"><rect x="2" y="2" width="12" height="12" rx="2" fill="none" stroke="var(--accent-green)" stroke-width="2"/></svg>brambleworksdesk</li>
    </ul>
    <div class="brand-front">
      <div class="brand-front__dot"></div>
      <p class="brand-front__name">BrambleWorks</p>
    </div>
  </section>

  <section class="card card--back">
    <div class="brand-back">
      <div class="brand-back__dot"></div>
      <div class="brand-back__text">
        <p class="brand-back__name">BrambleWorks</p>
        <div class="brand-back__rule"></div>
        <p class="brand-back__tagline">Student Success Platform</p>
      </div>
    </div>
  </section>
</main>
</body>
</html>
```